Glimmerseal pond linings website template

We need a template for our new website. Glimmerseal is currently marketed through www.tarpavale.com.au, and we are moving the pond/dam linings to a dedicated site www.glimmerseal.com.au

The site is essentially brochureware. The content (less landing page & photo gallery) is on the new site to give you a better idea of what we do. We are also on Facebook.com/glimmerseal

We are looking for a template/style which we can adapt to the different sections of the site as required. We also get a lot of phone/tablet visitors so an alternative mobile layout would be a bonus, but by no means required.

I am proficient in HTML/CSS & javascript so can code most designs thrown at me.

Any icons or interface fonts should be freely available web fonts where possible.

Target Market(s)

We are targeting both landscape professionals (design & construction) as well as the DIY market for ponds/wateragrdens.

Industry/Entity Type

Moving

Requirements
Must have
• We need a design (preferably layered PSD or AI) as basis for our overall site look and feel. Fonts/iconography/layout are where we are lacking. We can do the HTML/CSS/JS/PHP internally.
Nice to have
• A style guide either in file or separate would be nice.
Layers with effect (i.e.. :hover, CSS3 transition endpoints, etc)

```html
<!DOCTYPE html>
<html lang="en">
<head>
<meta charset="utf-8">
<title>Glimmerseal – Pond Liners</title>
<link href="https://fonts.googleapis.com/css2?family=Open+Sans:wght@400;600;700&display=swap" rel="stylesheet">
<style>
:root{
  --nav-green:#1d6a3c;
  --heading-blue:#1f4f8c;
  --navy:#163a6e;
  --lime:#9fbf2e;
  --band:#eef6d8;
  --text:#4a4a4a;
  --line:#c9d3bf;
  --white:#ffffff;
  --water:#bfe3ef;
}
*{margin:0;padding:0;box-sizing:border-box}
html,body{width:1200px;height:1157px;overflow:hidden;background:var(--white)}
body{font-family:"Open Sans",Arial,sans-serif;color:var(--text)}
.page{position:relative;width:1200px;height:1157px;overflow:hidden}
.abs{position:absolute}

.brand{left:163px;top:28px;display:flex;align-items:center;gap:10px}
.brand-square{width:34px;height:34px;background:var(--lime)}
.brand-name{font-size:34px;font-weight:600;color:var(--nav-green);letter-spacing:1px;line-height:1}

.consult{right:150px;top:34px;text-align:right}
.consult-line{font-size:13px;color:var(--navy)}
.consult-call{margin-top:6px;display:flex;align-items:center;justify-content:flex-end;gap:10px;font-size:19px;font-weight:700;color:var(--navy)}
.consult-call .num{color:var(--nav-green)}

.main-nav{top:115px;left:0;width:1200px;height:20px}
.main-nav a{position:absolute;font-size:12px;color:var(--nav-green);text-decoration:none;font-weight:600;letter-spacing:.1px}
.search{left:870px;top:112px;width:184px;height:23px;border:1px solid #d6d6d6;font-size:10.5px;color:#666;padding:4px 10px}
.search svg{position:absolute;right:6px;top:4px}

.hero-band{left:0;top:156px;width:1200px;height:423px;background:var(--band)}
.tile{position:absolute}

.section-title{font-size:14.5px;color:var(--heading-blue);letter-spacing:.3px}
.section-rule{height:1px;background:var(--line)}
.about-text{left:168px;top:638px;width:562px;font-size:11.6px;line-height:14.6px;color:var(--text)}
.features{left:172px;top:768px;list-style:none}
.features li{height:26.5px;font-size:12.6px;color:var(--navy);display:flex;align-items:center;gap:7px}

.thumb{position:absolute;width:138px;height:132px;background:#f4f4f4;border:1px solid #d4d4d4;box-shadow:0 1px 2px rgba(0,0,0,.12);padding:6px}
.thumb div{width:100%;height:100%}

.footer-band{left:0;top:1034px;width:1200px;height:123px;background:var(--band)}
.footer-art{left:740px;top:970px;width:350px;height:150px;background:linear-gradient(90deg,var(--band),var(--water))}
.footer-brand{left:174px;top:1010px;display:flex;align-items:center;gap:8px}
.footer-brand .brand-square{width:24px;height:24px}
.footer-brand .brand-name{font-size:24px}
.foot-small{font-size:11.6px;color:#555}
.follow{left:452px;top:1048px;font-size:10.5px;color:#555}
.social{position:absolute;top:1070px;width:24px;height:24px;border-radius:3px}
.contact-lines{left:557px;top:1047px;font-size:11px;color:#555;line-height:22px}
</style>
</head>
<body>
<div class="page">

  <div class="abs brand">
    <span class="brand-square"></span>
    <span class="brand-name">Glimmerseal</span>
  </div>

  <div class="abs consult">
    <div class="consult-line">Schedule Your Free Consultation Today</div>
    <div class="consult-call">
      <svg width="28" height="28" viewBox="0 0 28 28" aria-hidden="true"><path d="M4 16 A10 10 0 0 1 24 16" fill="none" stroke="#163a6e" stroke-width="3"/><rect x="2" y="15" width="6" height="9" rx="2" fill="#163a6e"/><rect x="20" y="15" width="6" height="9" rx="2" fill="#163a6e"/><path d="M23 24 Q22 27 16 27" fill="none" stroke="#163a6e" stroke-width="2"/></svg>
      <span>Call <span class="num">+61 3 9555 0142</span></span>
    </div>
  </div>

  <nav class="abs main-nav">
    <a style="left:162px">HOME</a>
    <a style="left:224px">ABOUT US</a>
    <a style="left:307px">HAPPENINGS</a>
    <a style="left:403px">GALLERY</a>
    <a style="left:481px">LINER STYLES</a>
    <a style="left:580px">PREPARATION</a>
    <a style="left:680px">INSTALLATION</a>
    <a style="left:782px">CONTACT US</a>
  </nav>
  <div class="abs search">Search in our site
    <svg width="14" height="14" viewBox="0 0 14 14" aria-hidden="true"><circle cx="8.5" cy="5.5" r="4.2" fill="none" stroke="#777" stroke-width="1.4"/><line x1="5.5" y1="8.5" x2="1.5" y2="12.5" stroke="#777" stroke-width="1.6"/></svg>
  </div>

  <div class="abs hero-band"></div>
  <div class="tile" role="img" aria-label="Weatherboard house with trees" style="left:149px;top:156px;width:204px;height:210px;background:linear-gradient(180deg,#9cc3e4,#6f7d5a 55%,#3e4a35)"></div>
  <div class="tile" role="img" aria-label="Green garden panel with plant motif" style="left:149px;top:368px;width:204px;height:211px;background:linear-gradient(160deg,#7fa64a,#5d8a2e)"></div>
  <div class="tile" role="img" aria-label="Backyard deck beside a lily pond" style="left:355px;top:156px;width:396px;height:423px;background:linear-gradient(180deg,#b7d6ee 0%,#d9d2c4 35%,#8e7a62 60%,#3f5a73 100%)"></div>
  <div class="tile" role="img" aria-label="Green panel with fish motif" style="left:752px;top:156px;width:134px;height:108px;background:linear-gradient(160deg,#9cbf6a,#6d9a3c)"></div>
  <div class="tile" role="img" aria-label="Rock waterfall into pond" style="left:752px;top:266px;width:134px;height:106px;background:linear-gradient(180deg,#7b7564,#4d5a3d 60%,#2f3d35)"></div>
  <div class="tile" role="img" aria-label="Pond garden in front of house" style="left:888px;top:156px;width:165px;height:216px;background:linear-gradient(180deg,#a7c07a,#5d7a3a 55%,#33452a)"></div>
  <div class="tile" role="img" aria-label="Installation crew laying pond liner" style="left:752px;top:373px;width:301px;height:206px;background:linear-gradient(180deg,#cfd0c8 0%,#8e8e86 30%,#3a3a3c 60%,#1f1f22 100%)"></div>

  <div class="abs section-title" style="left:168px;top:600px">ABOUT US</div>
  <div class="abs section-rule" style="left:168px;top:626px;width:72px"></div>
  <p class="abs about-text">Glimmerseal has been manufactured, marketed and installed throughout Australia and the Pacific Rim since the early 1980's for a variety of domestic and commercial applications. Glimmerseal pond liners put an end to the complicated and time consuming installation used by other methods. Simply excavate or construct the desired shape of your pond pool or water garden, indoor or outdoor, place your Glimmerseal into position and secure the edges. It can easily be completed in a weekend.</p>

  <div class="abs section-title" style="left:168px;top:733px">UNIQUE FEATURES</div>
  <div class="abs section-rule" style="left:168px;top:757px;width:128px"></div>
  <ul class="abs features">
    <li><svg width="8" height="10" viewBox="0 0 8 10" aria-hidden="true"><path d="M1 1 L4 5 L1 9 M4 1 L7 5 L4 9" fill="none" stroke="#163a6e" stroke-width="1.3"/></svg>20 Years Guarantee</li>
    <li><svg width="8" height="10" viewBox="0 0 8 10" aria-hidden="true"><path d="M1 1 L4 5 L1 9 M4 1 L7 5 L4 9" fill="none" stroke="#163a6e" stroke-width="1.3"/></svg>Very Economical</li>
    <li><svg width="8" height="10" viewBox="0 0 8 10" aria-hidden="true"><path d="M1 1 L4 5 L1 9 M4 1 L7 5 L4 9" fill="none" stroke="#163a6e" stroke-width="1.3"/></svg>Fix it Forget it- Completely Maintenance Free</li>
    <li><svg width="8" height="10" viewBox="0 0 8 10" aria-hidden="true"><path d="M1 1 L4 5 L1 9 M4 1 L7 5 L4 9" fill="none" stroke="#163a6e" stroke-width="1.3"/></svg>Work with our clients on an individual basis</li>
    <li><svg width="8" height="10" viewBox="0 0 8 10" aria-hidden="true"><path d="M1 1 L4 5 L1 9 M4 1 L7 5 L4 9" fill="none" stroke="#163a6e" stroke-width="1.3"/></svg>Long lasting</li>
  </ul>

  <svg class="abs" style="left:474px;top:758px" width="124" height="124" viewBox="0 0 124 124" aria-hidden="true">
    <circle cx="62" cy="62" r="61" fill="#163a6e"/>
    <circle cx="62" cy="62" r="36" fill="#ffffff"/>
    <path d="M45 62 L57 74 L80 50" fill="none" stroke="#163a6e" stroke-width="8" stroke-linecap="round"/>
  </svg>

  <svg class="abs" style="left:764px;top:600px" width="30" height="24" viewBox="0 0 30 24" aria-hidden="true">
    <rect x="1" y="4" width="28" height="19" rx="3" fill="#1e7fd0"/>
    <rect x="10" y="1" width="10" height="5" rx="1" fill="#1e7fd0"/>
    <circle cx="15" cy="13.5" r="6.5" fill="#fff"/><circle cx="15" cy="13.5" r="4" fill="#1e7fd0"/>
  </svg>
  <div class="abs section-title" style="left:807px;top:604px">GALLERY</div>

  <div class="thumb" style="left:764px;top:638px"><div role="img" aria-label="Rock-edged pond" style="background:linear-gradient(180deg,#9a7a5a,#6f7a5e 55%,#a39a8a)"></div></div>
  <div class="thumb" style="left:909px;top:638px"><div role="img" aria-label="Stepping stones across pond" style="background:linear-gradient(180deg,#6d7a4e,#8a9aa8 50%,#5a5048)"></div></div>
  <div class="thumb" style="left:764px;top:776px"><div role="img" aria-label="Landscaped pond with boulders and trees" style="background:linear-gradient(180deg,#3f78c8,#8fb0d8 35%,#5e7a45 70%,#9a9280)"></div></div>
  <div class="thumb" style="left:909px;top:776px"><div role="img" aria-label="Crew installing liner with machinery" style="background:linear-gradient(180deg,#8a8a80,#c9b23a 50%,#4a4a44)"></div></div>

  <div class="abs footer-band"></div>
  <div class="abs footer-art" role="img" aria-label="Footer illustration of water, reeds and stones"></div>

  <div class="abs footer-brand">
    <span class="brand-square"></span>
    <span class="brand-name">Glimmerseal</span>
  </div>
  <div class="abs foot-small" style="left:174px;top:1071px">Copyright © 2013-2014 Glimmerseal Australia</div>
  <div class="abs foot-small" style="left:174px;top:1099px">Contact Us | Copyright Notice</div>

  <div class="abs follow">FOLLOW US ON</div>
  <span class="social" style="left:454px;background:#5fb8e6"></span>
  <span class="social" style="left:483px;background:#3b5c9e"></span>

  <div class="abs contact-lines">
    <div>Phone - 1300 555 210</div>
    <div>International Phone - +61 3 9555 0142</div>
    <div>Fax - 1300 555 318</div>
    <div>International Fax - +61 3 9555</div>
  </div>

</div>
</body>
</html>
```